Afternoon Soiree Garden Party Invitation

Invitation design for an 'Afternoon Soirée' backyard garden party.
Format is for-print and mailing and can be either double-sided design to be enveloped and mailed or it can be a postcard-style with design on one side and address/postage placeholder on the reverse side.
Text, dimensions and additional information in the provided Word document.
Font styles to use
Script
Requirements
Must have
- Elegant, yet easy-going and warm/welcoming feel

```html
<!DOCTYPE html>
<html lang="en">
<head>
<meta charset="utf-8">
<title>Afternoon Soirée Invitation</title>
<link rel="stylesheet" href="https://fonts.googleapis.com/css2?family=Cormorant+Garamond:wght@400;500;600&family=Sacramento&display=swap">
<style>
  :root {
    --backdrop: #f1efeb;
    --navy: #18213a;
    --navy-deep: #141c33;
    --gold: #b8875a;
    --gold-line: #a97d52;
    --ivory: #f4f1ea;
    --border-green: #2c4a3f;
    --border-teal: #24384f;
    --border-rust: #6b3a2f;
    --border-rose: #9a6a68;
  }
  * { margin: 0; padding: 0; box-sizing: border-box; }
  html, body {
    width: 1200px; height: 1200px; overflow: hidden;
    background: var(--backdrop);
  }
  .canvas { position: relative; width: 1200px; height: 1200px; }

  .invitation {
    position: absolute; left: 251px; top: 60px;
    width: 697px; height: 1080px;
    box-shadow: 0 6px 18px rgba(0,0,0,0.18);
  }
  .painted-border {
    position: absolute; inset: 0;
    background:
      radial-gradient(ellipse at 15% 10%, var(--border-green) 0%, transparent 45%),
      radial-gradient(ellipse at 90% 35%, var(--border-rust) 0%, transparent 45%),
      radial-gradient(ellipse at 10% 60%, var(--border-rose) 0%, transparent 35%),
      radial-gradient(ellipse at 95% 75%, var(--border-rose) 0%, transparent 30%),
      radial-gradient(ellipse at 50% 100%, var(--border-green) 0%, transparent 50%),
      var(--border-teal);
  }
  .panel {
    position: absolute; left: 50px; right: 48px; top: 42px; bottom: 37px;
    background: linear-gradient(180deg, var(--navy) 0%, var(--navy-deep) 100%);
  }
  .panel-frame {
    position: absolute; left: 27px; right: 27px; top: 22px; bottom: 22px;
    border: 1.5px solid var(--gold-line);
  }

  .line {
    position: absolute; left: 0; width: 100%;
    text-align: center; white-space: nowrap;
    font-family: "Cormorant Garamond", Georgia, serif;
  }
  .title-eyebrow {
    top: 90px; left: 110px; width: auto; text-align: left;
    padding-left: 104px;
    font-size: 38px; letter-spacing: 3px; color: var(--gold); font-weight: 500;
  }
  .title-script {
    top: 100px; left: 100px; width: auto; text-align: left;
    font-family: "Sacramento", cursive;
    font-size: 128px; color: var(--ivory); line-height: 1;
  }
  .venue { top: 268px; font-size: 26px; letter-spacing: 1.5px; color: var(--ivory); line-height: 31px; }
  .weekday { top: 363px; font-size: 23px; letter-spacing: 1px; color: var(--gold); font-weight: 600; }
  .date { top: 440px; font-size: 62px; letter-spacing: 2px; color: var(--ivory); font-weight: 500; }
  .time { top: 552px; font-size: 24px; color: var(--ivory); font-weight: 600; letter-spacing: 0.5px; }
  .weather { top: 584px; font-size: 19px; letter-spacing: 1px; color: var(--gold); }
  .sprig {
    position: absolute; left: 220px; top: 812px; width: 150px; height: 56px;
    border-radius: 50%;
    background: radial-gradient(ellipse, rgba(244,241,234,0.35) 0%, rgba(244,241,234,0) 70%);
  }
  .note { top: 885px; font-size: 19px; color: var(--gold); line-height: 25px; letter-spacing: 0.3px; }
</style>
</head>
<body>
<div class="canvas">
  <article class="invitation">
    <div class="painted-border" role="img" aria-label="Painted garden foliage and flowers in deep greens, teals, rust and rose"></div>
    <section class="panel">
      <div class="panel-frame"></div>
      <p class="line title-eyebrow">AFTERNOON</p>
      <h1 class="line title-script">Soirée</h1>
      <p class="line venue">MARLOWE RESIDENCE<br>428 LINDEN AVE.</p>
      <p class="line weekday">FRIDAY</p>
      <p class="line date">07.17.2020</p>
      <p class="line time">4:00 PM - 8:00 PM</p>
      <p class="line weather">WEATHER PERMITTING</p>
      <div class="sprig" role="img" aria-label="Small hand-drawn botanical sprig ornament"></div>
      <p class="line note">Please call 555-204-7381 if unsure.<br>This is a 19+ event.</p>
    </section>
  </article>
</div>
</body>
</html>
```